Pixel Harbor Business Card

I have attached several examples of business cards that I have seen online that I liked. We will be incorporating Spot UV coating and raised ink on the cards. Optionally we may use embossing with color. The business card will be used for 3d printing services. We are hoping to see some different color options of cards (i.e. black card, white card, etc.). We look forward to your ideas.

• Dorian Kest
Founder and CEO
+1.555.000.0000 cell
+1.000.000.0001 office
+1.000.000.0001 fax
Dorian.Kest@3dVorlanix.example
www.3dVorlanix.example
• I would be nice to see some 3d background designs to add some depth to the designs of the cards since it is a 3d design company. There are examples of this in the files I have attached.

```html
<!DOCTYPE html>
<html lang="en">
<head>
<meta charset="utf-8">
<title>Vorlanix Business Card</title>
<link rel="stylesheet" href="https://fonts.googleapis.com/css2?family=Josefin+Sans:wght@300&family=Libre+Baskerville&family=Questrial&display=swap">
<style>
  :root {
    --canvas: #e9eaec;
    --card-white: #ffffff;
    --ink: #2b2b2b;
    --ink-soft: #555555;
    --accent: #d81b72;
    --rule: #c9c9c9;
    --art-yellow: #fdd22a;
    --art-orange: #f48a1f;
    --art-red: #e8303a;
    --art-magenta: #c2277a;
    --art-pale: #fff4c8;
  }
  * { box-sizing: border-box; margin: 0; padding: 0; }
  html, body {
    width: 1200px; height: 1000px; overflow: hidden;
    background: var(--canvas);
  }
  .stage { position: relative; width: 1200px; height: 1000px; }

  .card {
    position: absolute; top: 469px;
    width: 486px; height: 258px;
    overflow: hidden;
    box-shadow: 0 6px 18px rgba(0,0,0,.18);
  }
  .card--front { left: 124px; }
  .card--back { left: 693px; background: var(--card-white); }

  .card__art { position: absolute; }
  .card--front .card__art {
    inset: 0;
    background:
      linear-gradient(155deg, transparent 30%, rgba(194,39,122,.75) 55%, transparent 75%),
      radial-gradient(ellipse at 70% 20%, var(--art-magenta), transparent 55%),
      linear-gradient(120deg, var(--art-red) 0%, var(--art-orange) 35%, var(--art-yellow) 65%, var(--art-orange) 100%);
  }
  .card--back .card__art {
    top: 0; right: 0; width: 340px; height: 258px;
    background:
      radial-gradient(ellipse at 55% 25%, rgba(232,48,58,.85), transparent 45%),
      radial-gradient(ellipse at 85% 70%, var(--art-yellow), transparent 60%),
      linear-gradient(100deg, rgba(255,255,255,1) 0%, rgba(255,244,200,.6) 30%, var(--art-orange) 70%, var(--art-yellow) 100%);
  }

  .brand { position: absolute; display: flex; align-items: center; gap: 8px; }
  .brand__dot { border-radius: 50%; }
  .brand__name {
    font-family: "Josefin Sans", sans-serif; font-weight: 300;
    text-transform: uppercase; letter-spacing: .3em;
  }
  .card--front .brand {
    left: 0; right: 0; top: 72px; flex-direction: column; gap: 12px;
  }
  .card--front .brand__dot { width: 70px; height: 70px; background: #2a2a2a; }
  .card--front .brand__name { color: #fff; font-size: 21px; padding-left: .3em; }

  .card--back .brand { left: 26px; top: 22px; flex-direction: column; align-items: flex-start; gap: 8px; }
  .card--back .brand__dot { width: 44px; height: 44px; background: #2a2a2a; margin-left: 26px; }
  .card--back .brand__name { color: var(--ink-soft); font-size: 12px; }

  .person { position: absolute; left: 26px; top: 104px; }
  .person__name { font-family: "Libre Baskerville", serif; font-size: 20px; color: var(--ink); }
  .person__role { font-family: "Questrial", sans-serif; font-size: 9px; color: var(--ink-soft); margin-top: 1px; padding-left: 2px; }

  .rule { position: absolute; left: 28px; width: 168px; border-top: 1px dotted var(--rule); }
  .rule--top { top: 141px; }
  .rule--mid { top: 200px; }

  .contacts { position: absolute; left: 30px; list-style: none;
    font-family: "Questrial", sans-serif; font-size: 8px; color: var(--ink-soft); }
  .contacts--phone { top: 154px; }
  .contacts--online { top: 210px; }
  .contacts li { display: flex; align-items: center; height: 11px; }
  .contacts svg { width: 8px; height: 8px; fill: var(--accent); margin-right: 14px; }
  .contacts__label { width: 40px; }
</style>
</head>
<body>
<main class="stage">

  <section class="card card--front">
    <div class="card__art" role="img" aria-label="Abstract layered 3D shards in magenta, red, orange and yellow"></div>
    <div class="brand">
      <span class="brand__dot"></span>
      <span class="brand__name">Vorlanix</span>
    </div>
  </section>

  <section class="card card--back">
    <div class="card__art" role="img" aria-label="Abstract 3D shards in red, orange and yellow fading into white"></div>
    <div class="brand">
      <span class="brand__dot"></span>
      <span class="brand__name">Vorlanix</span>
    </div>

    <div class="person">
      <p class="person__name">DORIAN Kest</p>
      <p class="person__role">Founder &amp; CEO</p>
    </div>

    <div class="rule rule--top"></div>
    <ul class="contacts contacts--phone">
      <li><svg viewBox="0 0 10 10"><path d="M2 0h2l1 3-1.5 1a6 6 0 0 0 2.5 2.5L7 5l3 1v2c0 1-1 2-2 2A8 8 0 0 1 0 2c0-1 1-2 2-2z"/></svg><span class="contacts__label">Cell</span><span>: +1.555.000.0000</span></li>
      <li><svg viewBox="0 0 10 10"><path d="M3 1h4v2h3v6H0V3h3zM4 2v1h2V2z"/></svg><span class="contacts__label">Office</span><span>: +1.000.000.0001</span></li>
      <li><svg viewBox="0 0 10 10"><path d="M2 0h6v3h2v5H8v2H2V8H0V3h2zM3 6v3h4V6z"/></svg><span class="contacts__label">Fax</span><span>: +1.000.000.0001</span></li>
    </ul>
    <div class="rule rule--mid"></div>
    <ul class="contacts contacts--online">
      <li><svg viewBox="0 0 10 10"><path d="M0 2h10v6H0zM1 3l4 3 4-3v-.3H1z"/></svg><span class="contacts__label">E-mail</span><span>: Dorian.Kest@3dVorlanix.example</span></li>
      <li><svg viewBox="0 0 10 10"><path d="M5 0a5 5 0 1 0 0 10A5 5 0 0 0 5 0zm0 2a3 3 0 1 1 0 6 3 3 0 0 1 0-6z"/></svg><span class="contacts__label">Web</span><span>: www.3dVorlanix.example</span></li>
    </ul>
  </section>

</main>
</body>
</html>
```